Header für Blog zur Organisationsentwicklung
LunaKrie hat die Hinweise im Briefing und in den Kommentaren zu vorhandenen Designs gut aufgenommen und den Gestaltungsprozess vorangetrieben. So bekomme ich ein tolles Design, wo ich vorher keine Ahnung hatte, wie es aussehen sollte.
Zielgruppe
Ich bin freiberuflicher Organisationsberater und pflege auf meiner Website ein Blog zur Organisationsentwicklung. Dieses Blog soll zukünftig auf einer eigenen Domain erscheinen, sodass auch andere Kollegen sich daran beteiligen können. Daher soll mein Name nicht mehr im Vordergrund stehen - wenngleich ich immer noch als der Macher des Blog erkennbar bleiben soll.
Aufgabenstellung
Für das Blog "Labor für Unternehmenswandel" www.uw-labor.de wird ein ansprechender Header gesucht.
Der Header sollte den Namen des Blog und ein grafisches Element enthalten, dass der Bildsprache "Werkstatt", "Organisation", "Führung", etc. entnommen ist. Eventuell ein Element, das die Bildsprachen verbindet?
Da das Blog von einem Foto-Slider unter dem Header geprägt ist, sollte der Header nicht einfach aus einem Foto bestehen.
Die Farbgebung des Blog stellt die grafische Verbindung zu meiner Website www.hasselkamp.com her.
Mein Logo sollte im Header nicht verwendet werden, da ich das Blog bewusst von meiner Website löse, um weitere Beraterkollegen einzuladen, dabei mitzumachen

```html
<!DOCTYPE html>
<html lang="de">
<head>
<meta charset="utf-8">
<title>Labor für Unternehmenswandel – Header</title>
<link href="https://fonts.googleapis.com/css2?family=Source+Sans+3:wght@600&display=swap" rel="stylesheet">
<style>
  :root {
    --navy: #2f2e6a;
    --panel: #5a5a8b;
    --panel-light: #6a6a98;
    --white: #ffffff;
  }
  html, body {
    margin: 0;
    padding: 0;
    overflow: hidden;
    background: var(--navy);
  }
  .blog-header {
    position: relative;
    width: 1200px;
    height: 102px;
    background: var(--navy);
    overflow: hidden;
  }
  .blog-header__backdrop {
    position: absolute;
    inset: 0;
  }
  .blog-header__icons {
    position: absolute;
    inset: 0;
  }
  .blog-header__title {
    position: absolute;
    left: 360px;
    top: 0;
    height: 102px;
    display: flex;
    align-items: center;
    margin: 0;
    font-family: "Source Sans 3", "Source Sans Pro", sans-serif;
    font-weight: 600;
    font-size: 35px;
    letter-spacing: 0.2px;
    color: var(--white);
  }
</style>
</head>
<body>
<header class="blog-header">
  <svg class="blog-header__backdrop" width="1200" height="102" viewBox="0 0 1200 102" aria-hidden="true">
    <defs>
      <linearGradient id="panelShade" x1="0" y1="0" x2="1" y2="1">
        <stop offset="0" stop-color="var(--panel-light)"/>
        <stop offset="1" stop-color="var(--panel)"/>
      </linearGradient>
    </defs>
    <path d="M0 0 H368 C330 30 292 62 262 102 H0 Z" fill="url(#panelShade)"/>
  </svg>

  <svg class="blog-header__icons" width="1200" height="102" viewBox="0 0 1200 102" aria-hidden="true">
    <!-- wrench tile -->
    <g class="icon icon--wrench" transform="translate(47 43)">
      <rect width="31" height="31" rx="5" fill="var(--white)"/>
      <path d="M22.5 5.5 a5.5 5.5 0 0 0 -6.2 7.2 L6.5 22.5 a2 2 0 0 0 2.8 2.8 L19.1 15.5 a5.5 5.5 0 0 0 7.2 -6.2 l-3.2 3.2 -3 -0.8 -0.8 -3 Z" fill="var(--navy)"/>
    </g>
    <!-- org chart tile -->
    <g class="icon icon--orgchart" transform="translate(111 15)">
      <rect width="32" height="32" rx="5" fill="var(--white)"/>
      <g fill="var(--navy)">
        <rect x="12.5" y="6" width="7" height="6" rx="1"/>
        <rect x="15.3" y="12" width="1.5" height="4"/>
        <rect x="7" y="15.5" width="18" height="1.5"/>
        <rect x="7" y="15.5" width="1.5" height="4"/>
        <rect x="15.3" y="15.5" width="1.5" height="4"/>
        <rect x="23.5" y="15.5" width="1.5" height="4"/>
        <rect x="4.5" y="19.5" width="6.5" height="6" rx="1"/>
        <rect x="12.75" y="19.5" width="6.5" height="6" rx="1"/>
        <rect x="21" y="19.5" width="6.5" height="6" rx="1"/>
      </g>
    </g>
    <!-- person tile -->
    <g class="icon icon--person" transform="translate(175 43)">
      <rect width="33" height="33" rx="5" fill="var(--white)"/>
      <g fill="var(--navy)">
        <circle cx="16.5" cy="11.5" r="5.5"/>
        <path d="M6.5 27 v-3 a6 6 0 0 1 6 -6 h8 a6 6 0 0 1 6 6 v3 Z"/>
      </g>
    </g>
  </svg>

  <h1 class="blog-header__title">Labor für Unternehmenswandel</h1>
</header>
</body>
</html>
```